Stationary Design Letterhead and Envelope

Artist should provide Letterhead and envelop stationary designs

Info for stationary:
Fenwarde Outdoor Advertising
4857 Mesa Rd. 318 N. PO BOX 582917
Austin, TX 78651

Dale Fenwarde
President
512-608-2917
dale@fenwardeoutdoor.example
fenwardeoutdoor.example

Target Market(s)

clients

Colors
0054AA
0677BA
7BADD7
CADEEF
E8F1F8

Requirements
Must have
• high quality unique eye catching and dynamic

```html
<!DOCTYPE html>
<html lang="en">
<head>
<meta charset="utf-8">
<title>Fenwarde Outdoor Advertising – Stationery</title>
<link href="https://fonts.googleapis.com/css2?family=Montserrat:wght@500;600&family=Open+Sans:wght@400&display=swap" rel="stylesheet">
<style>
:root{
  --brand-blue:#2271a3;
  --ink:#1d1d1d;
  --body-ink:#444;
  --paper:#f4f4f4;
  --backdrop:#e6e6e6;
  --link-blue:#0677ba;
}
*{margin:0;padding:0;box-sizing:border-box}
html,body{width:1200px;height:795px;overflow:hidden;background:var(--backdrop)}
.canvas{position:relative;width:1200px;height:795px;font-family:'Open Sans',sans-serif}
.sheet{position:absolute;background:var(--paper);overflow:hidden}

/* wordmark */
.wordmark{display:flex;align-items:center;gap:4px;font-family:'Montserrat',sans-serif;font-weight:600;color:var(--ink);line-height:1;white-space:nowrap}
.wordmark .mark{background:var(--brand-blue);flex:none}
.wordmark .name{display:flex;flex-direction:column;align-items:center}
.wordmark.on-blue{color:#fff}
.wordmark.on-blue .mark{background:#fff}

/* letterhead */
.letterhead{left:293px;top:99px;width:292px;height:414px}
.letterhead .wordmark{position:absolute;left:26px;top:25px}
.letterhead .wordmark .mark{width:9px;height:9px}
.letterhead .wordmark .name span:first-child{font-size:15px;letter-spacing:.3px}
.letterhead .wordmark .name span:last-child{font-size:5.6px;margin-top:2px}
.contact-list{position:absolute;left:179px;top:26px;list-style:none;font-family:'Montserrat',sans-serif;font-weight:500;font-size:5.6px;color:var(--body-ink);line-height:7.4px;white-space:nowrap}
.contact-list li{display:flex;align-items:center;gap:2px}
.contact-list svg{width:5px;height:5px;fill:var(--brand-blue)}
.letter-body{position:absolute;left:26px;top:91px;width:241px;font-size:5.25px;line-height:8px;color:var(--body-ink);text-align:justify}
.letter-body p{margin-bottom:8px}
.signature{position:absolute;left:26px;top:300px;width:36px;height:32px;background:#e9e9e9}
.letter-footer{position:absolute;left:0;right:0;top:387px;text-align:center;font-family:'Montserrat',sans-serif;font-weight:500;font-size:5.6px;line-height:7px;color:var(--body-ink)}
.letter-footer .company{color:var(--link-blue)}

/* folder */
.folder{left:637px;top:80px;width:346px;height:437px;background:var(--brand-blue)}
.folder .band{position:absolute;left:0;right:0;top:165px;height:105px;background:var(--paper);display:flex;align-items:center;justify-content:center}
.folder .wordmark{gap:7px}
.folder .wordmark .mark{width:18px;height:18px}
.folder .wordmark .name span:first-child{font-size:33px;letter-spacing:.5px}
.folder .wordmark .name span:last-child{font-size:11.5px;margin-top:4px}
.folder .web{position:absolute;left:0;right:0;top:394px;text-align:center;color:#fff;font-family:'Montserrat',sans-serif;font-weight:500;font-size:11px}

/* business cards */
.card-front{left:187px;top:551px;width:132px;height:75px;background:var(--brand-blue);display:flex;align-items:center;justify-content:center}
.card-front .wordmark .mark{width:5px;height:5px}
.card-front .wordmark .name span:first-child{font-size:11px}
.card-front .wordmark .name span:last-child{font-size:4.3px;margin-top:1.5px}
.card-back{left:187px;top:646px;width:132px;height:75px}
.card-back .wordmark{position:absolute;left:10px;top:32px;gap:3px}
.card-back .wordmark .mark{width:4px;height:4px}
.card-back .wordmark .name span:first-child{font-size:7px}
.card-back .wordmark .name span:last-child{font-size:2.9px;margin-top:1.2px}
.card-back .divider{position:absolute;left:68px;top:19px;width:1px;height:38px;background:#ccc}
.card-back .details{position:absolute;left:73px;top:19px;width:56px;font-family:'Montserrat',sans-serif;font-size:2.7px;line-height:4px;color:var(--body-ink);white-space:nowrap}
.card-back .person{font-weight:600;font-size:4px;color:var(--ink)}
.card-back .role{color:var(--link-blue);margin-bottom:3px}
.card-back .gap{margin-top:2px}

/* envelopes */
.envelope-front{left:353px;top:561px;width:329px;height:157px}
.envelope-front .wordmark{position:absolute;left:24px;top:24px}
.envelope-front .wordmark .mark{width:6px;height:6px}
.envelope-front .wordmark .name span:first-child{font-size:12px}
.envelope-front .wordmark .name span:last-child{font-size:4.6px;margin-top:1.5px}
.envelope-front .return-address{position:absolute;left:24px;top:47px;width:84px;text-align:center;font-family:'Montserrat',sans-serif;font-weight:500;font-size:4.2px;line-height:6px;color:var(--body-ink);white-space:nowrap}
.envelope-back{left:713px;top:561px;width:329px;height:157px}
.envelope-back svg.flap{position:absolute;left:0;top:0}
.envelope-back .wordmark{position:absolute;left:0;right:0;top:18px;justify-content:center}
.envelope-back .wordmark .mark{width:6px;height:6px}
.envelope-back .wordmark .name span:first-child{font-size:13px}
.envelope-back .wordmark .name span:last-child{font-size:5px;margin-top:1.5px}
</style>
</head>
<body>
<main class="canvas">

  <article class="sheet letterhead">
    <div class="wordmark"><span class="mark"></span><div class="name"><span>FENWARDE</span><span>OUTDOOR ADVERTISING</span></div></div>
    <ul class="contact-list">
      <li><svg viewBox="0 0 10 10"><path d="M2 0l2 2.5-1 1.2a6 6 0 0 0 3.3 3.3l1.2-1L10 8l-1.5 2A8.5 8.5 0 0 1 0 1.5z"/></svg>512-608-2917</li>
      <li><svg viewBox="0 0 10 10"><path d="M0 2h10v6H0zM0 2l5 3.5L10 2" stroke="#fff" stroke-width=".8"/></svg>dale@fenwardeoutdoor.example</li>
      <li><svg viewBox="0 0 10 10"><circle cx="5" cy="5" r="4.5" fill="none" stroke="#2271a3"/><path d="M.5 5h9M5 .5c-2.5 3-2.5 6 0 9M5 .5c2.5 3 2.5 6 0 9" fill="none" stroke="#2271a3" stroke-width=".7"/></svg>www.fenwardeoutdoor.example</li>
    </ul>
    <div class="letter-body">
      <p>Dear customer,</p>
      <p>Lorem ipsum dolor sit amet, consectetur adipisicing elit, sed do eiusmod tempor incididunt ut labore et dolore magna aliqua. Ut enim ad minim veniam, quis nostrud exercitation ullamco laboris nisi ut aliquip ex ea commodo consequat. Duis aute irure dolor in reprehenderit in voluptate velit esse cillum dolore eu fugiat nulla pariatur. Excepteur sint occaecat cupidatat non proident, sunt in culpa qui officia deserunt mollit anim id est laborum.</p>
      <p>Lorem ipsum dolor sit amet, consectetur adipisicing elit, sed do eiusmod tempor incididunt ut labore et dolore magna aliqua. Ut enim ad minim veniam, quis nostrud exercitation ullamco laboris nisi ut aliquip ex ea commodo consequat. Duis aute irure dolor in reprehenderit in voluptate velit esse cillum dolore eu fugiat nulla pariatur. Excepteur sint occaecat cupidatat non proident, sunt in culpa qui officia deserunt mollit anim id est laborum.</p>
      <p>Lorem ipsum dolor sit amet, consectetur adipisicing elit, sed do eiusmod tempor incididunt ut labore et dolore magna aliqua. Ut enim ad minim veniam, quis nostrud exercitation ullamco laboris nisi ut aliquip ex ea commodo consequat. Duis aute irure dolor in reprehenderit in voluptate velit esse cillum dolore eu fugiat nulla pariatur. Excepteur sint occaecat cupidatat non proident, sunt in culpa qui officia deserunt mollit anim id est laborum.</p>
      <p>Lorem ipsum dolor sit amet, consectetur adipisicing elit, sed do eiusmod tempor incididunt ut labore et dolore magna aliqua. Ut enim ad minim veniam, quis nostrud exercitation ullamco laboris nisi ut aliquip ex ea commodo consequat. Duis aute irure dolor in reprehenderit.</p>
      <p>Yours Sincerely,</p>
    </div>
    <div class="signature" role="img" aria-label="Handwritten signature of the sender"></div>
    <footer class="letter-footer">
      <div class="company">Fenwarde Outdoor Advertising</div>
      <div>4857 Mesa Rd. 318 N. PO BOX 582917 Austin, TX 78651</div>
    </footer>
  </article>

  <section class="sheet folder">
    <div class="band">
      <div class="wordmark"><span class="mark"></span><div class="name"><span>FENWARDE</span><span>OUTDOOR ADVERTISING</span></div></div>
    </div>
    <div class="web">www.fenwardeoutdoor.example</div>
  </section>

  <section class="sheet card-front">
    <div class="wordmark on-blue"><span class="mark"></span><div class="name"><span>FENWARDE</span><span>OUTDOOR ADVERTISING</span></div></div>
  </section>

  <section class="sheet card-back">
    <div class="wordmark"><span class="mark"></span><div class="name"><span>FENWARDE</span><span>OUTDOOR ADVERTISING</span></div></div>
    <div class="divider"></div>
    <div class="details">
      <div class="person">DALE FENWARDE</div>
      <div class="role">President</div>
      <div>4857 Mesa Rd. 318 N.</div>
      <div>PO BOX 582917 Austin,</div>
      <div>TX 78651</div>
      <div class="gap">512-608-2917</div>
      <div>dale@fenwardeoutdoor.example</div>
      <div>www.fenwardeoutdoor.example</div>
    </div>
  </section>

  <section class="sheet envelope-front">
    <div class="wordmark"><span class="mark"></span><div class="name"><span>FENWARDE</span><span>OUTDOOR ADVERTISING</span></div></div>
    <div class="return-address">4857 Mesa Rd. 318 N. PO BOX 582917<br>Austin, TX 78651</div>
  </section>

  <section class="sheet envelope-back">
    <svg class="flap" width="329" height="57" viewBox="0 0 329 57"><path d="M0 0H329L323 50Q322 55 316 55H13Q8 55 7 50Z" fill="#2271a3"/></svg>
    <div class="wordmark on-blue"><span class="mark"></span><div class="name"><span>FENWARDE</span><span>OUTDOOR ADVERTISING</span></div></div>
  </section>

</main>
</body>
</html>
```